Redesign wellness clinic website

The project is redesign a wellness clinic http://www.brambleviewwellness.com. The new website is to be responsive,clean,bright and a strong call to action which is to book an appointment. The logo will remain the same but the colour scheme on the website should be reflect purple white and green. I want it to be bright and cheerful and the feeling of clarity. The website shouldn't be overloaded with content but more visuals.

Target Market(s)

Anyone that has corporate wellness benefits within the downtown Toronto core. Majority of audience are professional working in Media, Telecommunications and Investments.

Industry/Entity Type

Health And Wellness

Number of Pages Required

5+ page

Font styles to use
Sans Serif

Colors
ffffff
886aae
acd036

Requirements
Must have
• -Strong call to action which is book an appointment like this page https://www.kelpwavephysio.com/
• -Services provided icons on the page like https://www.brightstepwellnessclinic.com/
• - Pictures of a good visualizing a fit and healthy life
• - Strong ratings from Quibb, Zorvik, TownJot, similar to this website http://www.truestridehealthclinic.ca/our-team-professionals/
• - Bright and clear
Should not have
• -No black and white images (redo our pictures)
• -Dark themes

```html
<!DOCTYPE html>
<html lang="en">
<head>
<meta charset="utf-8">
<title>Brambleview Wellness Centre</title>
<link href="https://fonts.googleapis.com/css2?family=Raleway:wght@400;500;600;700&family=Open+Sans:wght@400;600;700&display=swap" rel="stylesheet">
<style>
:root{
  --purple:#886aae;
  --purple-deep:#6b3f8c;
  --purple-band:#8a4ea6;
  --green:#acd036;
  --white:#ffffff;
  --ink:#222222;
  --muted:#555555;
  --grey-bg:#ececee;
  --footer:#1f1f21;
  --footer-text:#9a9a9e;
  --star:#f2b01e;
}
*{margin:0;padding:0;box-sizing:border-box}
html,body{width:1200px;height:3974px;overflow:hidden}
body{position:relative;background:var(--white);font-family:"Open Sans",Arial,sans-serif;color:var(--ink)}
.abs{position:absolute}
h1,h2,h3,.brand{font-family:"Raleway",Arial,sans-serif}

/* header */
.site-header{top:0;left:0;width:1200px;height:118px;background:var(--white)}
.brand-mark{left:62px;top:22px;width:64px;height:64px;border-radius:50%;background:var(--purple)}
.brand{left:140px;top:34px;font-size:21px;font-weight:700;color:var(--purple-deep)}
.brand-sub{left:200px;top:66px;font-size:15px;font-weight:600;color:var(--green)}
.call{left:480px;top:32px;display:flex;gap:14px;align-items:center}
.call small{display:block;font-size:12px;color:var(--muted)}
.call strong{display:block;font-size:25px;font-weight:600;color:var(--ink)}
.hours{left:715px;top:36px;display:flex;gap:12px;font-size:12px;line-height:17px;color:var(--ink)}
.social{left:945px;top:14px;display:flex;gap:14px}
.social span{width:12px;height:12px;background:#9a9a9e;border-radius:2px}
.btn-book{left:972px;top:48px;width:168px;height:44px;background:var(--green);color:var(--ink);font-weight:600;font-size:14px;display:flex;align-items:center;justify-content:center}

/* nav */
.main-nav{top:118px;left:0;width:1200px;height:50px;background:var(--purple-deep);display:flex;padding-left:60px}
.main-nav a{color:var(--white);text-decoration:none;font-size:13.5px;font-weight:600;padding:0 22px;display:flex;align-items:center;letter-spacing:.3px}
.main-nav a.active{background:#111}

/* hero */
.hero{top:168px;left:0;width:1200px;height:452px;background:linear-gradient(90deg,#6a4a3c 0%,#a57a62 35%,#d8b6a0 65%,#c7a187 100%)}
.hero h1{left:60px;top:68px;font-size:50px;line-height:52px;font-weight:600;color:var(--white);text-transform:uppercase}
.hero p{left:60px;top:180px;width:600px;font-size:14px;line-height:21px;color:var(--white)}
.hero .btn{left:60px;top:236px;width:212px;height:50px;background:var(--green);color:var(--ink);font-size:14px;font-weight:600;display:flex;align-items:center;justify-content:center}

/* about */
.about-band{top:705px;left:0;width:1200px;height:515px;background:var(--purple-band)}
.about-card{top:620px;left:60px;width:1080px;height:540px;background:var(--white);box-shadow:0 4px 20px rgba(0,0,0,.08)}
.about-card h2{left:45px;top:58px;font-size:42px;font-weight:600;color:var(--ink)}
.about-card p{left:45px;top:130px;width:470px;font-size:15px;line-height:26px;color:var(--ink)}
.video{left:548px;top:135px;width:482px;height:268px;background:linear-gradient(135deg,#eef2f4,#cdd8dc 60%,#8fa6ae)}
.video-bar{left:548px;top:373px;width:482px;height:30px;background:rgba(20,20,20,.75)}
.about-photo{left:20px;top:330px;width:340px;height:250px;background:linear-gradient(180deg,#f3e3d6,#e7c7b1 55%,#f7f7f7)}

/* services */
.services-title{top:1325px;left:0;width:1200px;text-align:center;font-size:33px;font-weight:500}
.services-sub{top:1370px;left:0;width:1200px;text-align:center;font-size:14px;color:var(--muted)}
.service-grid{top:1440px;left:60px;width:1080px;height:606px;display:grid;grid-template-columns:repeat(3,1fr);grid-template-rows:repeat(2,1fr)}
.service{display:flex;flex-direction:column;align-items:center;padding-top:52px;text-align:center}
.service.purple{background:linear-gradient(135deg,#d7c3e8,#c6a9dd)}
.service.green{background:linear-gradient(135deg,#e2f0bc,#cfe69a)}
.service .icon{width:60px;height:60px;background:var(--white);display:flex;align-items:center;justify-content:center;margin-bottom:16px}
.service h3{font-size:19px;font-weight:500;margin-bottom:14px}
.service p{width:290px;font-size:12.5px;line-height:19px;color:#333}

/* testimonials */
.testimonials{top:2115px;left:0;width:1200px;height:515px;background:var(--grey-bg)}
.testimonials h2{left:60px;top:40px;font-size:42px;font-weight:500}
.quote{left:60px;width:518px;height:150px;background:#f7f7f8;box-shadow:0 2px 8px rgba(0,0,0,.06)}
.quote .avatar{left:32px;top:36px;width:76px;height:76px;border-radius:50%;background:linear-gradient(135deg,#c99a7c,#6b4a3a)}
.quote p{left:128px;top:34px;width:360px;font-size:13px;line-height:21px;color:#333}
.quote .name{left:128px;top:118px;font-size:10px;font-weight:700;letter-spacing:.5px}
.spa-art{left:600px;top:0;width:600px;height:515px;background:radial-gradient(circle at 50% 45%,#f6d4ec 0%,#e6a9d4 30%,#ececee 70%)}

/* blog */
.blog{top:2630px;left:0;width:1200px;height:550px;background:linear-gradient(90deg,#b27ec4,var(--purple-band) 60%,#7a3f98)}
.blog-art{left:0;top:0;width:560px;height:550px;background:linear-gradient(160deg,#e7bde0,#c27fbe 50%,#9a5aa8)}
.blog h2{left:615px;top:58px;font-size:40px;font-weight:500;color:var(--white)}
.post{left:618px;width:522px;height:165px;background:var(--white);display:flex}
.post .thumb{width:172px;height:165px;flex:none;background:linear-gradient(135deg,#d8c8c0,#8a6a5c)}
.post .body{padding:12px 16px}
.post .date{font-size:11px;color:#333}
.post h3{font-size:18px;font-weight:600;margin:2px 0 8px}
.post p{font-size:11.5px;line-height:17px;color:#888}
.post .time{margin-top:8px;font-size:11px;color:#999}

/* ratings */
.ratings{top:3225px;left:60px;width:1080px;height:155px;display:flex;justify-content:space-between}
.rating{width:245px;height:155px;border:1px solid #ddd;display:flex;flex-direction:column;align-items:center;justify-content:center;gap:10px}
.rating .name{font-family:"Raleway",Arial,sans-serif;font-size:40px;font-weight:700;color:var(--purple-deep)}
.badge{width:110px;height:120px;background:#e8a24a}

/* location */
.location{top:3435px;left:0;width:1200px;height:135px;background:var(--green)}
.location h2{left:60px;top:22px;font-size:36px;font-weight:500}
.location p{left:60px;top:80px;width:700px;font-size:14px;line-height:20px}
.location .btn{left:950px;top:42px;width:190px;height:48px;background:#111;color:var(--white);font-size:15px;display:flex;align-items:center;justify-content:center}

/* footer */
.site-footer{top:3570px;left:0;width:1200px;height:404px;background:var(--footer);color:var(--footer-text)}
.f-mark{left:68px;top:40px;width:56px;height:56px;border-radius:50%;border:3px solid #7d7d82}
.f-brand{left:135px;top:58px;font-size:17px;font-weight:700;color:#d8d8dc}
.f-about{left:68px;top:128px;width:300px;font-size:12px;line-height:18px}
.f-contact{left:68px;top:200px;font-size:12px;line-height:32px}
.f-contact div{display:flex;align-items:center;gap:10px}
.f-col{top:60px;font-size:12.5px;line-height:32px}
.f-col h4{color:var(--white);font-size:13px;letter-spacing:1.5px;margin-bottom:10px;font-weight:600;line-height:20px}
.f-col h4::after{content:"";display:block;width:26px;height:2px;background:var(--white);margin-top:12px}
.newsletter{left:805px;top:128px;width:335px;height:42px;background:#2e2e31;display:flex;align-items:center;justify-content:space-between;padding:0 12px;font-size:11px}
.newsletter b{color:var(--white);font-size:10px;letter-spacing:1px}
.partner{left:805px;top:190px;width:150px;height:100px;background:var(--white);display:flex;align-items:center;justify-content:center;color:var(--purple-deep);font-weight:700;font-size:15px;text-align:center}
.copyright{left:0;top:376px;width:1200px;height:28px;border-top:1px solid #333;text-align:center;font-size:11px;line-height:28px}
</style>
</head>
<body>

<header class="site-header abs">
  <div class="brand-mark abs"></div>
  <div class="brand abs">Brambleview Wellness Centre</div>
  <div class="brand-sub abs">Call 416-555-0172</div>
  <div class="call abs">
    <svg width="22" height="36" viewBox="0 0 22 36"><rect x="1" y="1" width="20" height="34" rx="3" fill="#8a4ea6"/><rect x="4" y="5" width="14" height="22" fill="#fff"/><circle cx="11" cy="31" r="2" fill="#fff"/></svg>
    <div><small>Call us Today!</small><strong>416-555-0172</strong></div>
  </div>
  <div class="hours abs">
    <svg width="30" height="30" viewBox="0 0 30 30"><rect x="2" y="5" width="26" height="23" rx="2" fill="#8a4ea6"/><rect x="5" y="11" width="20" height="14" fill="#fff"/></svg>
    <div>Monday - Friday 7:30am - 8pm<br>Saturday 10am - 5pm<br>Sunday 10am - 5pm</div>
  </div>
  <div class="social abs"><span></span><span></span><span></span><span></span><span></span></div>
  <div class="btn-book abs">Make Appointment</div>
</header>

<nav class="main-nav abs">
  <a class="active">HOME</a><a>FEES AND SERVICES</a><a>OUR STAFF</a><a>NEWS AND UPDATES</a><a>CORPORATE WELLNESS</a><a>FORMS</a><a>CONTACT US</a>
</nav>

<section class="hero abs" role="img" aria-label="Woman relaxing face down while receiving a back massage">
  <h1 class="abs">Do not wait<br>start healing today</h1>
  <p class="abs">Our Centre is committed to helping improve and extend the lives of as many people as possible in our community.</p>
  <div class="btn abs">Start Appointment today</div>
</section>

<div class="about-band abs"></div>
<section class="about-card abs">
  <h2 class="abs">About us</h2>
  <p class="abs">Our Centre is committed to helping improve and extend the lives of as many people as possible in our community. Lorem eiusmod pinboard in do umami readymade swag. Selfies handset crowdfund, drinking vinegar jean vinegar stumptown yr pop-up artisan sunt. Craft beer elit seitan exercitation, photo booth.</p>
  <div class="video abs" role="img" aria-label="Video still of a woman in a yoga lunge pose"></div>
  <div class="video-bar abs"><svg width="482" height="30"><path d="M12 9 L22 15 L12 21 Z" fill="#fff"/><rect x="34" y="13" width="300" height="4" fill="#888"/><rect x="34" y="13" width="60" height="4" fill="#acd036"/></svg></div>
  <div class="about-photo abs" role="img" aria-label="Smiling woman lying on a white towel at a spa"></div>
</section>

<h2 class="services-title abs">Come experience the secrets of relaxation</h2>
<p class="services-sub abs">Our Centre is committed to helping improve lives of as many people</p>
<section class="service-grid abs">
  <div class="service purple"><div class="icon"><svg width="30" height="30"><path d="M15 3v24M5 10h20M7 20h16" stroke="#333" stroke-width="3"/></svg></div><h3>Chiropractic</h3><p>Lorem eiusmod pinboard in do umami readymade swag. Selfies handset crowdfund, drinking vinegar jean vinegar stumptown</p></div>
  <div class="service green"><div class="icon"><svg width="30" height="30"><path d="M15 4 C9 13 7 17 7 20 a8 8 0 0 0 16 0 C23 17 21 13 15 4Z" fill="#333"/></svg></div><h3>Physiotherapy</h3><p>Lorem eiusmod pinboard in do umami readymade swag. Selfies handset crowdfund, drinking vinegar jean vinegar stumptown</p></div>
  <div class="service purple"><div class="icon"><svg width="30" height="30"><rect x="6" y="5" width="7" height="20" fill="#333"/><rect x="17" y="5" width="7" height="20" fill="#333"/></svg></div><h3>Osteopathy</h3><p>Lorem eiusmod pinboard in do umami readymade swag. Selfies handset crowdfund, drinking vinegar jean vinegar stumptown</p></div>
  <div class="service green"><div class="icon"><svg width="30" height="30"><rect x="7" y="5" width="14" height="20" rx="2" fill="#333"/><circle cx="21" cy="21" r="6" fill="#333" stroke="#fff" stroke-width="2"/></svg></div><h3>Nutrition and Lifestyle Medicine</h3><p>Lorem eiusmod pinboard in do umami readymade swag. Selfies handset crowdfund, drinking vinegar jean vinegar stumptown</p></div>
  <div class="service purple"><div class="icon"><svg width="30" height="30"><rect x="5" y="12" width="20" height="14" fill="#333"/><circle cx="15" cy="7" r="4" fill="#333"/></svg></div><h3>Massage Therapy</h3><p>Lorem eiusmod pinboard in do umami readymade swag. Selfies handset crowdfund, drinking vinegar jean vinegar stumptown</p></div>
  <div class="service green"><div class="icon"><svg width="30" height="30"><path d="M15 4 C11 10 11 18 15 26 C19 18 19 10 15 4Z M3 12 C6 20 10 24 15 26 C12 20 9 15 3 12Z M27 12 C24 20 20 24 15 26 C18 20 21 15 27 12Z" fill="#333"/></svg></div><h3>Active Rehabilitation</h3><p>Lorem eiusmod pinboard in do umami readymade swag. Selfies handset crowdfund, drinking vinegar jean vinegar stumptown</p></div>
</section>

<section class="testimonials abs">
  <h2 class="abs">Testimonials</h2>
  <div class="quote abs" style="top:130px">
    <div class="avatar abs" role="img" aria-label="Client portrait"></div>
    <p class="abs">This was the most exciting and pleasurable experience with a doctor. Thank you for your incredible care and professional approach to all customers.</p>
    <div class="name abs">ELENA MARSH</div>
  </div>
  <div class="quote abs" style="top:295px">
    <div class="avatar abs" role="img" aria-label="Client portrait"></div>
    <p class="abs">This was the most exciting and pleasurable experience with a doctor. Thank you for your incredible care and professional approach to all customers.</p>
    <div class="name abs">ELENA MARSH</div>
  </div>
  <div class="spa-art abs" role="img" aria-label="Pink lotus flower behind stacked black spa stones, an orchid, oil bottle and candle"></div>
</section>

<section class="blog abs">
  <div class="blog-art abs" role="img" aria-label="Woman in a graceful yoga backbend in front of a large pink lotus"></div>
  <h2 class="abs">From our Blog</h2>
  <article class="post abs" style="top:113px">
    <div class="thumb" role="img" aria-label="Person working out in a gym"></div>
    <div class="body"><div class="date">2 March,2017</div><h3>Thai Massage</h3><p>Curabitur elit eros, fringilla eget est non, porttitor pharetra risus. Praesent dapibus ne...</p><div class="time">December 2 @ 1:00 pm - 5:30 pm</div></div>
  </article>
  <article class="post abs" style="top:322px">
    <div class="thumb" role="img" aria-label="Woman smiling during a fitness class"></div>
    <div class="body"><div class="date">2 March,2017</div><h3>Yoga Classes</h3><p>Suspendisse venenatis tellus nec tincidunt venenatis. Aliquam viverra est sit amet ligula ...</p><div class="time">December 2 @ 2:30 pm - 5:00 pm</div></div>
  </article>
</section>

<svg width="0" height="0" class="abs" aria-hidden="true"><defs><path id="star" d="M14 1l4 9 9 1-7 6 2 10-8-5-8 5 2-10-7-6 9-1z"/></defs></svg>
<section class="ratings abs">
  <div class="rating"><div class="name">Zorvik</div>
    <svg width="170" height="28" viewBox="0 0 170 28"><g fill="#f2b01e"><use href="#star"/><use href="#star" x="35"/><use href="#star" x="70"/><use href="#star" x="105"/><use href="#star" x="140"/></g></svg></div>
  <div class="rating"><div class="name">Quibb</div>
    <svg width="170" height="28" viewBox="0 0 170 28"><g fill="#886aae"><use href="#star"/><use href="#star" x="35"/><use href="#star" x="70"/><use href="#star" x="105"/><use href="#star" x="140"/></g></svg></div>
  <div class="rating"><div class="name">TownJot</div></div>
  <div class="rating"><div class="badge" role="img" aria-label="Listing award badge"></div></div>
</section>

<section class="location abs">
  <h2 class="abs">Visit our new location</h2>
  <p class="abs">We are open for business at 7:30 am. Open 7 days a week! Ask one of our associates about our Referral Reward Program!</p>
  <div class="btn abs">See the Map</div>
</section>

<footer class="site-footer abs">
  <div class="f-mark abs"></div>
  <div class="f-brand abs brand">Brambleview Wellness Centre</div>
  <p class="f-about abs">Vivamus ullamcorper, justo in dictum ullamcorper, quam enim maximus sem, a sodales.</p>
  <div class="f-contact abs">
    <div><svg width="12" height="14"><path d="M6 0a5 5 0 0 1 5 5c0 4-5 9-5 9S1 9 1 5a5 5 0 0 1 5-5z" fill="#9a9a9e"/></svg>Maple Row, Toronto, ON M4W 1A1</div>
    <div><svg width="12" height="14"><path d="M2 1h3l1 4-2 1a8 8 0 0 0 4 4l1-2 4 1v3c0 1-1 2-2 2C5 14 0 9 0 3c0-1 1-2 2-2z" fill="#9a9a9e"/></svg>1-800-555-0148</div>
    <div><svg width="12" height="14"><path d="M0 7 12 1 9 13 6 9z" fill="#9a9a9e"/></svg>hello@brambleviewwellness.com</div>
  </div>
  <div class="f-col abs" style="left:435px"><h4>COMPANY</h4>Services<br>Team<br>About Us<br>Blog<br>Contacts</div>
  <div class="f-col abs" style="left:620px"><h4>SERVICES</h4>Web Design<br>Mobile Development<br>Programming<br>Branding &amp; Identity<br>Clients Support</div>
  <div class="f-col abs" style="left:805px"><h4>NEWSLETTER</h4></div>
  <div class="newsletter abs"><span>Enter Your Email</span><b>SUBSCRIBE</b></div>
  <div class="partner abs">Hollis Dental Centre</div>
  <div class="copyright abs">© 2017 brambleview wellness centre All Rights Reserved.</div>
</footer>

</body>
</html>
```